IT COMPANYcutting edge tec business card

we are IT company that building any apps.
we need business card in japanese and english
You don’t have to include all information in front one you can attach part of that information to back-side
company name : 株式会社ひかりの丘 (BRIGHTHILL Inc.)
concept : cutting-edge technology
role : 取締役 (director)
name : 呉 炫秀 (Oh Hyeonsuk)
post number : 154-0038
address : 東京都世田谷区西若葉台5-14-8 (5-14-8, Nishiwakabadai, Setagaya Ku, Tokyo To, 154-0038, Japan)
Tel:+81-3-5917-2846
Mobile:+81-80-7253-3169
Email : hoh@brighthill-lab.com
website : www.brighthill-lab.com

we dont have logo so please make it as well
we also looking for designer who can make homapage design.

Contact Information for Business Card

cutting-edge design and modern for IT

Font styles to use
Sans Serif

Colors
34a6d7
33b8a4
6092c4
3377b5
886aae
6b449b
b868aa
a64599

Requirements
Must have
• Simple but designed

```html
<!DOCTYPE html>
<html lang="ja">
<head>
<meta charset="utf-8">
<title>BRIGHTHILL Inc. — Business Card</title>
<link rel="stylesheet" href="https://fonts.googleapis.com/css2?family=Open+Sans:wght@400;600;700&family=Noto+Sans+JP:wght@400;700&display=swap">
<style>
  :root {
    --page-bg: #2a2a2c;
    --card-bg: #1d1d1f;
    --accent: #b356b8;
    --ink: #f2f2f2;
    --rule: #5a5a5e;
    --pattern-a: #232325;
    --pattern-b: #1b1b1d;
  }
  * { box-sizing: border-box; margin: 0; padding: 0; }
  html, body {
    width: 1200px; height: 1108px; overflow: hidden;
    background: var(--page-bg);
    font-family: "Open Sans", "Noto Sans JP", sans-serif;
  }
  .canvas {
    width: 1200px; height: 1108px;
    display: flex; justify-content: center; align-items: center; gap: 60px;
  }
  .card {
    width: 470px; height: 740px;
    background: var(--card-bg);
    border-radius: 24px;
    position: relative;
    overflow: hidden;
    box-shadow: 0 18px 40px rgba(0,0,0,.45);
  }
  /* front */
  .brand {
    position: absolute; top: 92px; left: 0; right: 0;
    display: flex; flex-direction: column; align-items: center;
  }
  .brand-circle {
    width: 108px; height: 108px; border-radius: 50%;
    border: 5px solid var(--accent);
  }
  .brand-name {
    margin-top: 18px;
    font-family: "Open Sans", sans-serif; font-weight: 700;
    font-size: 52px; letter-spacing: 1px; color: var(--accent);
  }
  .details {
    position: absolute; right: 50px; top: 350px; width: 330px;
    text-align: right; color: var(--ink);
    font-size: 17px; line-height: 1.45;
  }
  .person-name, .company-name {
    color: var(--accent); font-weight: 700; font-size: 17px;
  }
  .person-name span + span, .company-name span + span { margin-left: 22px; }
  .rule { height: 1px; background: var(--rule); width: 150px; margin: 10px 0 10px auto; }
  .label { color: var(--accent); }
  .domain { color: var(--accent); }
  .address { font-size: 16px; }
  /* back */
  .back-pattern {
    position: absolute; inset: 0;
    background: radial-gradient(circle at 40% 35%, var(--pattern-a), var(--pattern-b) 75%);
  }
  .back-brand {
    position: absolute; left: 0; right: 0; top: 470px;
    display: flex; align-items: center; justify-content: center; gap: 10px;
  }
  .back-brand .brand-circle { width: 30px; height: 30px; border-width: 3px; }
  .back-brand .brand-name { margin: 0; font-size: 20px; }
</style>
</head>
<body>
<main class="canvas">
  <section class="card card-front">
    <div class="brand">
      <div class="brand-circle"></div>
      <div class="brand-name">BRIGHTHILL</div>
    </div>
    <div class="details">
      <p class="person-name"><span>呉 炫秀</span><span>OH HYEONSUK</span></p>
      <p class="role">取締役&nbsp; Director</p>
      <div class="rule"></div>
      <p><span class="label">P:</span> +81-3-5917-2846</p>
      <p><span class="label">M:</span> +81-80-7253-3169</p>
      <p><span class="label">E:</span> hoh@brighthill-lab.com</p>
      <p>www.<span class="domain">brighthill-lab</span>.com</p>
      <div class="rule"></div>
      <p class="company-name"><span>株式会社ひかりの丘</span><span>BRIGHTHILL</span></p>
      <p class="address">東京都世田谷区西若葉台5-14-8</p>
      <p class="address">(5-14-8, Nishiwakabadai,</p>
      <p class="address">Setagaya Ku, Tokyo To, 154-0038, Japan)</p>
    </div>
  </section>
  <section class="card card-back">
    <div class="back-pattern" role="img" aria-label="Faint repeating brand pattern in dark grey tones"></div>
    <div class="back-brand">
      <div class="brand-circle"></div>
      <div class="brand-name">BRIGHTHILL</div>
    </div>
  </section>
</main>
</body>
</html>
```